Webpage Design_Telecommunications VOIP

BRV Linkworks Inc. Talk Made Simple.
Webpage/Homepage Design for Voiceover IP solution and Telecommunications company, looking to expand market and compete with larger providers.
He has a long standing local provider business with http://www.harborlane-example.com/ (You can see the logo there, blue cloud, phone pad) with tag Line: Communications Evolved in first rotation. You can also find layout and content for voiceover IP services, which is the focus for BRV Linkworks, so it can stand alone from Harborlane.

Target Market(s)

Malls, Doctors Offices, Retail, Hospitals, Car Dealers, Finance Services, HR Services, Insurance, Hotels, Travel Commerce, Government, Software Companies, Large Health Clubs/Country Clubs, Entertainment Venues, Quarrow Arena, Maplecrest Pines University/Colleges/Education.
See Product list on Talo (also Site inspiration) they set their site up based on different verticals, just to give you some inspiration.
http://talo-example.com/small-business/
http://talo-example.com/government/

Industry/Entity Type

Telecommunications

Number of Pages Required

1 page

Font styles to use
Sans Serif

Requirements
Must have
• Logo, Clean, Simple Strong Highlight services Navigation.
• Similar, competitive and current design like http://talo-example.com/
• Strong theme of Customer Service, but with modern competitive messaging.
• Fast, simple communication solutions/messages.
• Use of the Phone in the cloud graphic as an interactive feature.
• Contact form
• Pixelvault Image ID: 508342716
• Image ID: 634910275
• Image ID: 172605943
Nice to have
• Quick Service boxes for "PRICING" (to be supported with a smart form on our end)
Should not have
• Generic Images, of Professionals shaking hands, please chose images less expected.

```html
<!DOCTYPE html>
<html lang="en">
<head>
<meta charset="utf-8">
<title>BRV Linkworks – Talk Made Simple</title>
<link rel="stylesheet" href="https://fonts.googleapis.com/css2?family=Open+Sans:wght@300;400;600;700&display=swap">
<style>
:root{
  --blue:#5aa5dc;
  --ink:#222;
  --text:#555;
  --muted:#777;
  --dark-btn:#444;
  --line:#e2e2e2;
  --band:#f7f7f7;
  --footer:#efefef;
  --white:#fff;
}
*{box-sizing:border-box;margin:0;padding:0}
html,body{width:1200px;height:932px;overflow:hidden;background:var(--white)}
body{font-family:"Open Sans",Arial,sans-serif;color:var(--text);position:relative}
a{color:inherit;text-decoration:none}
ul{list-style:none}

.site-header{position:absolute;left:0;top:0;width:1200px;height:92px;background:var(--white)}
.brand{position:absolute;left:132px;top:20px;display:flex;align-items:center;gap:12px}
.brand-mark{width:44px;height:44px;border-radius:50%;background:var(--blue)}
.brand-name{font-size:36px;font-weight:400;color:var(--ink);letter-spacing:.5px;line-height:1}
.main-nav{position:absolute;top:16px;right:134px;display:flex;gap:30px;font-size:12.5px;color:#555}
.main-nav a.active{color:var(--blue)}
.header-actions{position:absolute;top:47px;right:134px;display:flex;gap:13px}
.outline-btn{height:28px;border:1px solid #ccc;padding:0 15px;display:flex;align-items:center;gap:6px;font-size:10.5px;color:#555}
.outline-btn svg{width:9px;height:9px}

.hero{position:absolute;left:0;top:92px;width:1200px;height:400px;overflow:hidden}
.hero-photo{position:absolute;inset:0;background:
  radial-gradient(ellipse at 50% 45%, #e6ebee 0%, #b8c4cc 35%, #6f8494 70%, #3b5063 100%)}
.hero-title{position:absolute;left:0;right:0;top:102px;text-align:center;font-size:110px;font-weight:300;color:var(--white);letter-spacing:2px;line-height:1}
.hero-cta{position:absolute;left:0;right:0;top:222px;text-align:center}
.hero-cta .dot{display:block;width:60px;height:60px;border-radius:50%;background:var(--blue);border:4px solid var(--white);margin:0 auto 10px}
.hero-cta span{display:block;font-size:12px;font-weight:600;color:#111;line-height:16px}
.slider-dots{position:absolute;top:371px;left:0;right:0;display:flex;justify-content:center;gap:15px}
.slider-dots i{width:9px;height:9px;border-radius:50%;background:var(--white);border:1.5px solid var(--white)}
.slider-dots i.current{background:transparent;box-shadow:inset 0 0 0 2px #6f8494}

.services{position:absolute;left:0;top:492px;width:1200px;height:199px}
.service{position:absolute;top:33px;width:420px}
.service.cloud{left:155px}
.service.voip{left:630px}
.service-icon{position:absolute;left:0;top:5px;width:52px;height:52px}
.service-body{position:absolute;left:71px;top:0;width:350px}
.service h2{font-size:24px;font-weight:400;color:var(--blue);line-height:1.1;margin-bottom:8px}
.service p{font-size:10.1px;line-height:16px;color:#666}
.service p a{color:#222;margin-left:4px}
.price-btn{display:inline-flex;align-items:center;justify-content:center;margin-top:15px;width:103px;height:35px;background:var(--dark-btn);color:var(--white);font-size:12px;margin-left:1px}
.divider{position:absolute;left:598px;top:33px;width:1px;height:130px;background:var(--line)}

.contact-band{position:absolute;left:0;top:691px;width:1200px;height:89px;background:var(--band);font-size:12px;color:var(--muted)}
.contact-item{position:absolute;top:37px;display:flex;align-items:center;gap:8px;white-space:nowrap}
.contact-item svg{width:11px;height:11px;fill:#888}
.socials{position:absolute;right:134px;top:32px;display:flex;gap:7px}
.socials span{width:26px;height:26px;border-radius:50%;background:#aaa}
.socials span:first-child{background:#2f5597}

.site-footer{position:absolute;left:0;top:780px;width:1200px;height:152px;background:var(--footer)}
.footer-col{position:absolute;top:26px}
.footer-col h3{font-size:13.5px;font-weight:400;color:#444;margin-bottom:5px}
.footer-col li{font-size:10px;color:#666;line-height:17.6px}
.footer-col li::before{content:"•";margin-right:5px;color:#888}
.copyright{position:absolute;right:136px;top:28px;font-size:10px;color:#666;word-spacing:2px}
.footer-brand{position:absolute;right:136px;top:56px;display:flex;align-items:center;gap:8px}
.footer-brand .brand-mark{width:30px;height:30px;background:#bbb}
.footer-brand .brand-name{font-size:20px;color:#666}
</style>
</head>
<body>

<header class="site-header">
  <a class="brand" href="#">
    <span class="brand-mark"></span>
    <span class="brand-name">BRV Linkworks</span>
  </a>
  <nav class="main-nav">
    <a class="active" href="#">Home</a>
    <a href="#">About us</a>
    <a href="#">Services</a>
    <a href="#">Solutions</a>
    <a href="#">Contact us</a>
  </nav>
  <div class="header-actions">
    <a class="outline-btn" href="#">Get Connected Today!</a>
    <a class="outline-btn" href="#"><svg viewBox="0 0 10 10"><path d="M2 0.5 3.6 2.6 2.7 3.6Q3.8 6 6.4 7.3L7.4 6.4 9.5 8 8.5 9.5Q4.5 9.5 1.8 6 0.3 3.6 0.5 1.5Z" fill="#777"/></svg>Call us on : 877-555-0142</a>
  </div>
</header>

<section class="hero">
  <div class="hero-photo" role="img" aria-label="Blurred data centre corridor with server racks and glowing bokeh lights"></div>
  <h1 class="hero-title">BRV LINKWORKS</h1>
  <a class="hero-cta" href="#"><b class="dot"></b><span>GET STARTED TODAY!</span></a>
  <div class="slider-dots"><i class="current"></i><i></i><i></i><i></i></div>
</section>

<section class="services">
  <article class="service cloud">
    <svg class="service-icon" viewBox="0 0 52 52" aria-hidden="true">
      <rect x="6" y="8" width="40" height="10" rx="3" fill="#5aa5dc"/>
      <rect x="6" y="21" width="40" height="10" rx="3" fill="#5aa5dc"/>
      <rect x="6" y="34" width="40" height="10" rx="3" fill="#5aa5dc"/>
      <circle cx="39" cy="13" r="2" fill="#fff"/><circle cx="39" cy="26" r="2" fill="#fff"/><circle cx="39" cy="39" r="2" fill="#fff"/>
    </svg>
    <div class="service-body">
      <h2>Cloud Service</h2>
      <p>Donec vestibulum odio sem, ac laoreet massa ullamcorper id. Donec molestie nisi et tellus hendrerit vehicula. Nunc eu ligula sed quam pulvinar maximus in vitae eros. Proin porta fermentum ipsum.<a href="#">More</a></p>
      <a class="price-btn" href="#">VIEW PRICING</a>
    </div>
  </article>
  <div class="divider"></div>
  <article class="service voip">
    <svg class="service-icon" viewBox="0 0 52 52" aria-hidden="true">
      <rect x="2" y="14" width="9" height="34" rx="3" fill="#5aa5dc"/>
      <rect x="14" y="4" width="34" height="44" rx="4" fill="#5aa5dc"/>
      <rect x="20" y="8" width="20" height="10" fill="#fff"/>
      <g fill="#fff">
        <rect x="20" y="24" width="5" height="5"/><rect x="28" y="24" width="5" height="5"/><rect x="36" y="24" width="5" height="5"/>
        <rect x="20" y="31" width="5" height="5"/><rect x="28" y="31" width="5" height="5"/><rect x="36" y="31" width="5" height="5"/>
        <rect x="20" y="38" width="5" height="5"/><rect x="28" y="38" width="5" height="5"/><rect x="36" y="38" width="5" height="5"/>
      </g>
    </svg>
    <div class="service-body">
      <h2>VOIP</h2>
      <p>Donec vestibulum odio sem, ac laoreet massa ullamcorper id. Donec molestie nisi et tellus hendrerit vehicula. Nunc eu ligula sed quam pulvinar maximus in vitae eros. Proin porta fermentum ipsum.<a href="#">More</a></p>
      <a class="price-btn" href="#">VIEW PRICING</a>
    </div>
  </article>
</section>

<section class="contact-band">
  <div class="contact-item" style="left:132px"><svg viewBox="0 0 10 12"><path d="M5 0A4 4 0 0 0 1 4C1 7 5 12 5 12S9 7 9 4A4 4 0 0 0 5 0ZM5 5.6A1.6 1.6 0 1 1 5 2.4 1.6 1.6 0 0 1 5 5.6Z"/></svg>24 Building name, Street name City - Zipcode</div>
  <div class="contact-item" style="left:467px"><svg viewBox="0 0 10 10"><path d="M2 0.5 3.6 2.6 2.7 3.6Q3.8 6 6.4 7.3L7.4 6.4 9.5 8 8.5 9.5Q4.5 9.5 1.8 6 0.3 3.6 0.5 1.5Z"/></svg>Call us on : 456 555 0187</div>
  <div class="contact-item" style="left:714px"><svg viewBox="0 0 12 9"><path d="M0 0H12V1L6 5 0 1ZM0 2.2 6 6.2 12 2.2V9H0Z"/></svg>Email : info@brvlink-example.com</div>
  <div class="socials"><span></span><span></span><span></span></div>
</section>

<footer class="site-footer">
  <div class="footer-col" style="left:132px"><h3>Links</h3><ul><li>Home</li><li>About us</li><li>Services</li><li>Solutions</li></ul></div>
  <div class="footer-col" style="left:260px"><h3>Services</h3><ul><li>Cloud Services</li><li>VOIP COnnections</li><li>Maintanance</li><li>Solutions</li></ul></div>
  <div class="footer-col" style="left:444px"><h3>Other Links</h3><ul><li>Terms and Conditions</li><li>Privacy Policy</li><li>Disclamiber</li><li>Sitemap</li></ul></div>
  <div class="footer-col" style="left:644px"><h3>Support</h3><ul><li>Customer Support</li><li>Live Chat With us</li><li>FAQ</li></ul></div>
  <p class="copyright">Copyright © 2016 BRV Linkworks. All rights reserved.</p>
  <div class="footer-brand"><span class="brand-mark"></span><span class="brand-name">BRV Linkworks</span></div>
</footer>

</body>
</html>
```